Website-Design für die neue Handtaschenmarke Marvona
Zielgruppe
Frauen und auch Männer, die ästhetisch ausgearbeitete und gleichzeitig zweckmäßige Handtaschen und Accessoires suchen. Frauen, die Einzelstücke nach ihren Wünschen und Bedürfnissen angefertigt haben wollen.
Aufgabenstellung
Es soll die Startseite für eine Website mit einem kleinen angebundenen Online-Shop entstehen.
Es gibt keine bestehende Website, nur das Logo steht fest.
Das detailierte Briefing finden Sie als PDF Dokument in der Anlage.

```html
<!DOCTYPE html>
<html lang="de">
<head>
<meta charset="utf-8">
<title>Marvona – Neuheiten</title>
<link rel="stylesheet" href="https://fonts.googleapis.com/css2?family=Lato:wght@400;700&display=swap">
<style>
  :root {
    --ink: #1a1a1a;
    --accent: #c0161f;
    --paper: #ffffff;
    --rule: #2a2a2a;
    --muted: #3a3a3a;
    --bag-deep: #27324a;
    --bag-mid: #3d4a66;
    --backdrop: #ecebe8;
  }
  * { margin: 0; padding: 0; box-sizing: border-box; }
  html, body { width: 1200px; height: 900px; overflow: hidden; background: var(--paper); }
  body { font-family: "Lato", sans-serif; color: var(--ink); position: relative; }

  .brand-mark {
    position: absolute; left: 131px; top: 33px;
    width: 94px; height: 94px; border: 2px solid var(--ink); border-radius: 50%;
  }
  .brand-name {
    position: absolute; left: 289px; top: 84px;
    font-size: 22px; font-weight: 400; letter-spacing: 7px; color: var(--ink);
  }
  .main-nav {
    position: absolute; left: 289px; top: 114px;
    font-size: 14px; font-weight: 700; letter-spacing: 1.2px; white-space: nowrap;
  }
  .main-nav a { color: var(--ink); text-decoration: none; }
  .main-nav a.is-active { color: var(--accent); }
  .main-nav .sep { margin: 0 5px; font-weight: 400; }

  .category-nav { position: absolute; left: 131px; top: 180px; list-style: none; }
  .category-nav li { font-size: 11.5px; font-weight: 700; letter-spacing: 1.6px; line-height: 21px; }
  .category-nav a { color: var(--ink); text-decoration: none; }
  .category-nav a.is-active { color: var(--accent); }

  .product-photo {
    position: absolute; left: 288px; top: 180px; width: 779px; height: 570px;
    background:
      radial-gradient(ellipse 48% 40% at 50% 60%, var(--bag-deep) 0%, var(--bag-mid) 70%, transparent 100%),
      var(--backdrop);
  }
  .product-bar {
    position: absolute; left: 288px; top: 759px; width: 779px;
    border-top: 1px solid var(--rule);
  }
  .product-title { position: absolute; left: 0; top: 11px; font-size: 12px; font-weight: 700; letter-spacing: 1.4px; white-space: nowrap; }
  .product-more { position: absolute; left: 0; top: 26px; font-size: 11px; letter-spacing: 1.6px; color: var(--muted); white-space: nowrap; }
  .pager { position: absolute; right: 0; top: 9px; font-size: 14px; display: flex; gap: 32px; }
  .pager a { color: var(--ink); text-decoration: none; }

  .share { position: absolute; left: 289px; top: 815px; display: flex; gap: 12px; }
  .share-item { width: 16px; height: 16px; background: var(--ink); }

  .footer-link {
    position: absolute; right: 133px; top: 866px;
    font-size: 11px; letter-spacing: 1.6px; color: var(--muted); text-decoration: none;
  }
</style>
</head>
<body>
  <div class="brand-mark" aria-hidden="true"></div>
  <div class="brand-name">MARVONA</div>

  <nav class="main-nav">
    <a href="#">KOLLEKTION</a><span class="sep">|</span><a href="#" class="is-active">SHOP</a><span class="sep">|</span><a href="#">AUFTRAGSFERTIGUNG</a><span class="sep">|</span><a href="#">ÜBER MARVONA</a><span class="sep">|</span><a href="#">BLOG</a><span class="sep">|</span><a href="#">KONTAKT</a>
  </nav>

  <ul class="category-nav">
    <li><a href="#" class="is-active">NEUHEITEN</a></li>
    <li><a href="#">TRAGETASCHEN</a></li>
    <li><a href="#">SCHULTERTASCHEN</a></li>
    <li><a href="#">KOFFER</a></li>
    <li><a href="#">LEDERTASCHEN</a></li>
  </ul>

  <div class="product-photo" role="img" aria-label="Produktfoto: dunkelblaue, gesmokte Stoffhandtasche mit Perlenstickerei vor hellem Hintergrund"></div>

  <div class="product-bar">
    <div class="product-title">HANDTASCHE 1</div>
    <div class="product-more">ZUSATZINFORMATIONEN</div>
    <div class="pager"><a href="#">&lt;</a><a href="#">&gt;</a></div>
  </div>

  <div class="share">
    <span class="share-item" aria-label="Teilen"></span>
    <span class="share-item" aria-label="Teilen"></span>
  </div>

  <a href="#" class="footer-link">KONTAKT &amp; IMPRESSUM</a>
</body>
</html>
```